K7 Teardown looking for leading edge design not typical for our industry

We need to incorporate our new company tag line "foundations, follow-through, fairness" into our cards. Im open to any type of design for this and colour treatment. In fact the whole card needs a new lay out including the back. "Sustainable Deconstruction" needs to be removed from the back and the new tagline used. Would like to see different text and treatment used for "Deconstruction & Demolition".

Target Market(s)

Construction

Industry/Entity Type

Construction Company

Contact Information for Business Card

Standard business card size

Font styles to use
Sans Serif

Colors
9bcb3c
0255a3
f37122

Requirements
Should not have
• Irregular sizing.

```html
<!DOCTYPE html>
<html lang="en">
<head>
<meta charset="utf-8">
<title>K7 Teardown — Business Cards</title>
<link rel="stylesheet" href="https://fonts.googleapis.com/css2?family=Open+Sans:wght@400;600;700&family=Oswald:wght@400;500&display=swap">
<style>
  :root {
    --green: #9bcb3c;
    --blue: #0255a3;
    --blue-deep: #0a3f7a;
    --orange: #f37122;
    --white: #ffffff;
    --stage: #eceae6;
    --ink-soft: #2a6cb0;
  }
  * { margin: 0; padding: 0; box-sizing: border-box; }
  html, body {
    width: 1200px; height: 913px; overflow: hidden;
    background: var(--stage);
    font-family: "Open Sans", Arial, sans-serif;
  }
  .stage { position: relative; width: 1200px; height: 913px; }

  .card {
    position: absolute;
    width: 520px; height: 297px;
    border-radius: 14px;
    overflow: hidden;
    background: var(--white);
    box-shadow: 0 10px 24px rgba(0,0,0,0.18);
  }
  .card-front { left: 50px; top: 150px; }
  .card-back { left: 630px; top: 466px; }
  .card svg.swoosh { position: absolute; inset: 0; width: 100%; height: 100%; }

  /* front */
  .holder { position: absolute; left: 30px; top: 40px; }
  .holder-name { font-weight: 700; font-size: 24px; color: var(--blue); line-height: 1.1; }
  .holder-role { font-weight: 600; font-size: 15px; color: var(--orange); margin-top: 2px; }

  .brand-front {
    position: absolute; right: 26px; top: 26px;
    display: flex; align-items: center; gap: 10px;
  }
  .brand-dot { width: 30px; height: 30px; border-radius: 50%; background: var(--blue); }
  .brand-name {
    font-family: "Oswald", Arial, sans-serif; font-weight: 500;
    font-size: 20px; color: var(--blue); letter-spacing: 0.5px; text-transform: uppercase;
    line-height: 1.05;
  }

  .contact {
    position: absolute; left: 30px; top: 180px;
    color: var(--white); font-size: 12px; line-height: 14.6px;
    list-style: none;
  }
  .contact li { display: flex; align-items: center; gap: 7px; white-space: nowrap; }
  .contact .address { padding-left: 0; }
  .contact svg { width: 11px; height: 11px; flex: none; }

  /* back */
  .brand-back {
    position: absolute; left: 0; right: 0; top: 70px;
    display: flex; flex-direction: column; align-items: center; gap: 14px;
  }
  .brand-back .brand-dot { width: 64px; height: 64px; }
  .brand-back .brand-name { font-size: 36px; }

  .tagline {
    position: absolute; right: 24px; bottom: 28px;
    font-family: "Oswald", Arial, sans-serif; font-weight: 500;
    font-size: 17px; letter-spacing: 0.6px; text-transform: uppercase;
    color: var(--white);
  }
  .tagline .t-green { color: var(--green); }
  .tagline .t-orange { color: var(--orange); }
</style>
</head>
<body>
<main class="stage">

  <section class="card card-front" aria-label="Business card front">
    <svg class="swoosh" viewBox="0 0 520 297" preserveAspectRatio="none" aria-hidden="true">
      <path d="M0,150 Q250,44 520,82 L520,297 L0,297 Z" fill="var(--orange)"/>
      <path d="M0,163 Q250,60 520,98 L520,297 L0,297 Z" fill="var(--blue)"/>
      <path d="M0,230 Q260,200 520,260 L520,297 L0,297 Z" fill="var(--blue-deep)" opacity="0.35"/>
    </svg>

    <div class="holder">
      <p class="holder-name">Marcus Hale</p>
      <p class="holder-role">Head Estimator</p>
    </div>

    <div class="brand-front">
      <span class="brand-dot"></span>
      <span class="brand-name">K7 Teardown<br>&amp; Demolition Inc</span>
    </div>

    <ul class="contact">
      <li class="address">#200, 4410-62 Street</li>
      <li class="address">Red Deer, AB T4N 1K3</li>
      <li>
        <svg viewBox="0 0 12 12" aria-hidden="true"><path d="M2.5 1 L4.5 1 L5.2 3.6 L4 4.6 Q5 7 7.4 8 L8.4 6.8 L11 7.5 L11 9.5 Q10.5 11 9 11 Q1 10 1 2.5 Q1 1 2.5 1 Z" fill="var(--orange)"/></svg>
        (555) 210.4410
      </li>
      <li>
        <svg viewBox="0 0 12 12" aria-hidden="true"><rect x="1" y="4" width="10" height="6" rx="1" fill="var(--orange)"/><rect x="3" y="1" width="6" height="3" fill="var(--orange)"/></svg>
        (555) 877.2193
      </li>
      <li>
        <svg viewBox="0 0 12 12" aria-hidden="true"><rect x="3" y="0.5" width="6" height="11" rx="1.2" fill="none" stroke="var(--orange)" stroke-width="1.3"/></svg>
        (555) 210.4418
      </li>
      <li>
        <svg viewBox="0 0 12 12" aria-hidden="true"><rect x="0.8" y="2.5" width="10.4" height="7" fill="none" stroke="var(--orange)" stroke-width="1.2"/><path d="M1 3 L6 7 L11 3" fill="none" stroke="var(--orange)" stroke-width="1.2"/></svg>
        marcush@k7teardown.com
      </li>
      <li>
        <svg viewBox="0 0 12 12" aria-hidden="true"><circle cx="6" cy="6" r="5" fill="none" stroke="var(--orange)" stroke-width="1.2"/><path d="M1 6 H11 M6 1 Q3 6 6 11 Q9 6 6 1" fill="none" stroke="var(--orange)" stroke-width="1"/></svg>
        www.k7teardown.com
      </li>
    </ul>
  </section>

  <section class="card card-back" aria-label="Business card back">
    <svg class="swoosh" viewBox="0 0 520 297" preserveAspectRatio="none" aria-hidden="true">
      <path d="M0,297 L0,282 Q330,262 520,168 L520,297 Z" fill="var(--blue)"/>
    </svg>

    <div class="brand-back">
      <span class="brand-dot"></span>
      <span class="brand-name">K7 Teardown</span>
    </div>

    <p class="tagline">
      <span class="t-green">Foundations</span>, <span class="t-orange">Follow-through</span>, Fairness
    </p>
  </section>

</main>
</body>
</html>
```